Design refresh of existing HR Application

Talvora is an HR & Payroll processing software, already in use by thousands of people. It is a feature packed, enterprise-grade software that is also simple and user friendly. Visit us at https://talvora.example

Seeking a refresh of the app design/UI.

Key objectives are to make it "sleeker", more professional and polished, whist still retaining functionality. Not intended to be a massive overhaul, but more of reorganization and improvements on design elements.

You may login to our demo account to see the app live.
https://app.talvora.example/login
User: demo@talvora.example
Password: Bex47

Target Market(s)

HR Managers, business administrators/owners and employees.

Industry/Entity Type

Business Software

Number of Pages Required

4 page

Font styles to use
Other font styles liked:
• Lato

Colors
0255a3
3377b5
00a990
33b8a4
f37122
faa54b

Requirements
Must have
• Must retain the current functionality on each page.
Nice to have
• Fine to suggest changes to colors, font sizes, card designs, moving sections around and any other design element changes.

```html
<!DOCTYPE html>
<html lang="en">
<head>
<meta charset="utf-8">
<title>Talvora – Calendar, weekly view</title>
<link href="https://fonts.googleapis.com/css2?family=Nunito+Sans:wght@400;600;700&display=swap" rel="stylesheet">
<style>
:root{
  --navy:#0255a3;--blue:#3377b5;--teal:#33b8a4;--orange:#f37122;--amber:#faa54b;
  --ink:#1f2a3a;--muted:#9aa3ae;--line:#e6e9ee;--panel:#f3f5f9;--white:#fff;
  --hours:#e4eefa;--hours-head:#7fa9d6;
}
*{box-sizing:border-box;margin:0;padding:0}
html,body{width:1200px;height:1200px;overflow:hidden}
body{background:var(--white);font-family:"Nunito Sans",sans-serif;color:var(--ink);position:relative}
.abs{position:absolute}
.brand{left:36px;top:38px;font-size:29px;font-weight:700;color:var(--navy)}
.greeting{left:162px;top:38px;font-size:29px;font-weight:400;color:var(--navy)}
.avatar{left:1131px;top:27px;width:33px;height:33px;border-radius:50%;background:radial-gradient(circle at 50% 40%,#8a6a58,#3a3a44)}
.avatar::after{content:"";position:absolute;right:-1px;top:1px;width:7px;height:7px;border-radius:50%;background:#2ecc71;border:1px solid #fff}
.nav{left:27px;top:0}
.nav-item{position:absolute;left:0;display:flex;align-items:center;gap:14px;font-size:12.5px;color:var(--muted);white-space:nowrap}
.nav-item svg{width:19px;height:19px;stroke:#b5bcc5;fill:none;stroke-width:1.4}
.nav-item.active{color:var(--navy);font-weight:600}
.nav-item.active svg{stroke:var(--navy)}
.nav-mark{left:160px;top:299px;width:3px;height:14px;background:var(--navy)}
.main{left:161px;top:108px;width:1001px;height:1120px;background:var(--panel);border-radius:12px}
.card{top:137px;width:220px;height:122px;background:var(--white);border-radius:4px;box-shadow:0 1px 3px rgba(0,0,0,.04)}
.tile{position:absolute;left:16px;top:17px;width:188px;height:89px;border-radius:3px;color:#fff;font-weight:700}
.tile.teal{background:var(--teal)}
.tile.blue{background:var(--blue);display:flex;flex-direction:column;align-items:center;justify-content:center;gap:4px;font-size:14px}
.tile .num{position:absolute;left:17px;top:10px;font-size:22px}
.tile .lbl{position:absolute;left:17px;top:44px;font-size:14px;line-height:15px}
.tile .ico{position:absolute;right:16px;top:15px}
.tile svg{stroke:#fff;fill:none;stroke-width:1.6}
.tab{top:280px;width:112px;height:39px;background:#dfe1e5;border-radius:4px 4px 0 0;font-size:12.5px;color:#b4b8be;display:flex;align-items:center;justify-content:center}
.tab.active{background:var(--white);color:var(--navy);font-size:15px;font-weight:600}
.tz-label{left:874px;top:285px;font-size:12.5px;color:#5d6673}
.tz{left:982px;top:276px;width:155px;height:34px;background:#fff;border:1px solid #dde1e6;border-radius:3px;font-size:12.5px;color:#8a929c;padding-left:8px;display:flex;align-items:center}
.tz::after{content:"";position:absolute;right:14px;top:14px;border:5px solid transparent;border-top:6px solid #555}
.sheet{left:185px;top:319px;width:952px;height:900px;background:var(--white)}
.filter{top:340px;height:34px;border:1px solid #dde1e6;border-radius:3px;font-size:8.5px;color:#8a929c;display:flex;align-items:center;padding-left:9px}
.filter .chev{position:absolute;right:9px;top:12px;width:10px;height:6px;stroke:#333;fill:none;stroke-width:1.6}
.sort{left:1085px;top:343px}
.week{left:215px;top:390px;width:264px;height:59px;background:var(--navy);color:#fff;font-size:14px;font-weight:600;display:flex;align-items:center;justify-content:space-between;padding:0 18px}
.days{left:479px;top:390px;width:629px;height:59px;display:grid;grid-template-columns:repeat(7,1fr);background:#e6f0fb}
.day{border-left:1px solid #fff;text-align:center;color:var(--navy);padding-top:9px}
.day b{display:block;font-size:12px;font-weight:600}
.day span{font-size:8.5px;font-weight:600}
.grid{left:215px;top:449px;width:893px;display:grid;grid-template-columns:220px 44px repeat(7,1fr)}
.duty{height:32px;display:flex;align-items:center;justify-content:center;font-size:9px;font-weight:600;color:var(--navy);border-bottom:1px solid var(--line)}
.duty.label{justify-content:flex-end;grid-column:1 / 3;padding-right:2px}
.person{height:66px;display:flex;align-items:center;gap:12px;padding-left:24px;border-bottom:1px solid var(--line)}
.badge{width:32px;height:32px;border-radius:4px;display:flex;align-items:center;justify-content:center}
.badge svg{stroke:#fff;fill:none;stroke-width:1.5}
.person b{display:block;font-size:10.5px;font-weight:600}
.person span{font-size:8.5px;color:#6e7784}
.hrs{height:66px;background:var(--hours);display:flex;align-items:center;justify-content:center;font-size:9px;font-weight:600;color:var(--navy);position:relative}
.hrs-head{position:absolute;left:0;top:0;width:100%;height:17px;background:var(--hours-head);color:#fff;font-size:8.5px;display:flex;align-items:center;justify-content:center;font-weight:600}
.cell{height:66px;border-left:1px solid var(--line);border-bottom:1px solid var(--line);position:relative}
.shift{position:absolute;inset:2px;display:flex;align-items:flex-end;justify-content:center;padding-bottom:9px;font-size:9px}
.s-purple{background:#f3e6fb;color:#a64fd9}
.s-sky{background:#ebf1fc;color:#5a8fe0}
.s-teal{background:#e2f7f2;color:#3cc0a8}
.s-blue{background:#d4e7fa;color:#4a86d8}
.s-peach{background:#fde8d6;color:#d29455}
.s-grey{background:#e4e4e4;color:#c2c2c2}
</style>
</head>
<body>
<div class="abs brand">Logo</div>
<div class="abs greeting">Good afternoon Demo, it's great to see you!</div>
<div class="abs avatar" role="img" aria-label="User profile photo"></div>

<nav class="abs nav">
  <div class="nav-item" style="top:678px;top:168px"><svg viewBox="0 0 20 20"><rect x="2" y="2" width="6" height="6"/><rect x="12" y="2" width="6" height="6"/><rect x="2" y="12" width="6" height="6"/><rect x="12" y="12" width="6" height="6"/></svg>Dashboard</div>
  <div class="nav-item" style="top:235px"><svg viewBox="0 0 20 20"><circle cx="10" cy="7" r="4"/><path d="M3 18c0-4 3-6 7-6s7 2 7 6z"/></svg>Employees</div>
  <div class="nav-item active" style="top:296px"><svg viewBox="0 0 20 20"><rect x="2" y="3" width="16" height="15"/><path d="M2 7h16M2 11h16M2 15h16M7 7v11M13 7v11M6 1v4M14 1v4"/></svg>Calendar</div>
  <div class="nav-item" style="top:360px"><svg viewBox="0 0 20 20"><path d="M3 2h14v16l-2-1.5-2 1.5-2-1.5-2 1.5-2-1.5-2 1.5z"/><path d="M10 6v6M7 14h6M12 5h3M12 9h3"/></svg>Expenses</div>
  <div class="nav-item" style="top:428px"><svg viewBox="0 0 20 20"><rect x="3" y="4" width="12" height="15"/><path d="M6 1h12v15M9 8v7M7 10h4"/></svg>Payroll</div>
  <div class="nav-item" style="top:496px"><svg viewBox="0 0 20 20"><path d="M7 2h6l-2 4h-2zM5 8h10l2 10H3z"/><path d="M10 10v6M8 12h4"/></svg>Loan</div>
  <div class="nav-item" style="top:563px"><svg viewBox="0 0 20 20"><path d="M4 2h9l4 4v12H4z"/><path d="M7 15v-3M10 15v-5M13 15v-4"/></svg>Reports</div>
  <div class="nav-item" style="top:631px"><svg viewBox="0 0 20 20"><circle cx="10" cy="10" r="3"/><circle cx="10" cy="10" r="7.5" stroke-dasharray="3 1.6"/></svg>Settings</div>
</nav>
<div class="abs nav-mark"></div>

<div class="abs main"></div>

<div class="abs card" style="left:188px"><div class="tile teal"><span class="num">28</span><span class="lbl">Event<br>Approvals</span>
  <svg class="ico" width="32" height="30" viewBox="0 0 32 30"><rect x="9" y="4" width="20" height="18"/><path d="M9 9h20M9 14h20M15 9v13M22 9v13M13 2v4M25 2v4"/><circle cx="8" cy="21" r="6" fill="#33b8a4"/><path d="M5 21l2 2 4-4"/></svg></div></div>
<div class="abs card" style="left:431px"><div class="tile teal"><span class="num">20</span><span class="lbl">Leave<br>Approval</span>
  <svg class="ico" width="30" height="30" viewBox="0 0 30 30"><ellipse cx="17" cy="9" rx="7" ry="8"/><path d="M17 1v16M14 17l1 4h4l1-4"/><circle cx="8" cy="21" r="6" fill="#33b8a4"/><path d="M5 21l2 2 4-4"/></svg></div></div>
<div class="abs card" style="left:674px"><div class="tile blue">
  <svg width="32" height="28" viewBox="0 0 32 28"><rect x="9" y="3" width="20" height="18"/><path d="M9 8h20M9 13h20M15 8v13M22 8v13M13 1v4M25 1v4"/><circle cx="8" cy="20" r="6" fill="#3377b5"/><path d="M8 17v6M5 20h6"/></svg>Add Event</div></div>
<div class="abs card" style="left:917px"><div class="tile blue">
  <svg width="30" height="28" viewBox="0 0 30 28"><ellipse cx="17" cy="8" rx="7" ry="7.5"/><path d="M17 1v15M14 16l1 4h4l1-4"/><circle cx="8" cy="20" r="6" fill="#3377b5"/><path d="M8 17v6M5 20h6"/></svg>Request Leave</div></div>

<div class="abs tab" style="left:185px">Daily</div>
<div class="abs tab active" style="left:304px">Weekly</div>
<div class="abs tab" style="left:423px">Monthly</div>
<div class="abs tab" style="left:542px">List</div>
<div class="abs tab" style="left:661px">Geo-Tagging</div>
<div class="abs tz-label">Select time zone</div>
<div class="abs tz">Current time zone</div>

<div class="abs sheet"></div>
<div class="abs filter" style="left:215px;width:131px">Search by name or nickname</div>
<div class="abs filter" style="left:350px;width:97px">Department<svg class="chev" viewBox="0 0 10 6"><path d="M1 1l4 4 4-4"/></svg></div>
<div class="abs filter" style="left:455px;width:97px">Branch<svg class="chev" viewBox="0 0 10 6"><path d="M1 1l4 4 4-4"/></svg></div>
<div class="abs filter" style="left:560px;width:97px">Group<svg class="chev" viewBox="0 0 10 6"><path d="M1 1l4 4 4-4"/></svg></div>
<div class="abs filter" style="left:665px;width:97px">Activity<svg class="chev" viewBox="0 0 10 6"><path d="M1 1l4 4 4-4"/></svg></div>
<div class="abs filter" style="left:770px;width:97px">Activity Type<svg class="chev" viewBox="0 0 10 6"><path d="M1 1l4 4 4-4"/></svg></div>
<div class="abs filter" style="left:875px;width:97px">Positions<svg class="chev" viewBox="0 0 10 6"><path d="M1 1l4 4 4-4"/></svg></div>
<div class="abs filter" style="left:980px;width:97px">First Name<svg class="chev" viewBox="0 0 10 6"><path d="M1 1l4 4 4-4"/></svg></div>
<svg class="abs sort" width="22" height="22" viewBox="0 0 22 22"><path d="M6 2v17M2 15l4 4 4-4" stroke="#0255a3" stroke-width="1.8" fill="none"/><text x="13" y="9" font-size="8.5" fill="#0255a3" font-family="Nunito Sans,sans-serif" font-weight="700">A</text><text x="13" y="20" font-size="8.5" fill="#0255a3" font-family="Nunito Sans,sans-serif" font-weight="700">Z</text></svg>

<div class="abs week"><svg width="8" height="12" viewBox="0 0 8 12"><path d="M6 1L1 6l5 5" stroke="#fff" fill="none" stroke-width="1.3"/></svg>Week 5 of May 2020<svg width="8" height="12" viewBox="0 0 8 12"><path d="M2 1l5 5-5 5" stroke="#fff" fill="none" stroke-width="1.3"/></svg></div>
<div class="abs days">
  <div class="day"><b>Mon</b><span>25/05/2020</span></div>
  <div class="day"><b>Tue</b><span>26/05/2020</span></div>
  <div class="day"><b>Wed</b><span>27/05/2020</span></div>
  <div class="day"><b>Thu</b><span>28/05/2020</span></div>
  <div class="day"><b>Fri</b><span>29/05/2020</span></div>
  <div class="day"><b>Sat</b><span>30/05/2020</span></div>
  <div class="day"><b>Sun</b><span>31/05/2020</span></div>
</div>

<div class="abs grid">
  <div class="duty label">On Duty</div>
  <div class="duty">140</div><div class="duty">140</div><div class="duty">113</div><div class="duty">134</div><div class="duty">160</div><div class="duty">52</div><div class="duty"></div>

  <div class="person"><div class="badge" style="background:#b057e8"><svg width="16" height="16" viewBox="0 0 16 16"><circle cx="8" cy="5" r="3.2"/><path d="M2 15c0-3.5 2.7-5.5 6-5.5s6 2 6 5.5z"/></svg></div><div><b>01 Employee</b><span>Branch B | Department 6</span></div></div>
  <div class="hrs"><div class="hrs-head">Hours</div>40</div>
  <div class="cell"><div class="shift s-purple">10:00 - 19:00</div></div>
  <div class="cell"><div class="shift s-sky">10:00 - 19:00</div></div>
  <div class="cell"><div class="shift s-teal">10:00 - 19:00</div></div>
  <div class="cell"><div class="shift s-blue">10:00 - 19:00</div></div>
  <div class="cell"><div class="shift s-peach">10:00 - 19:00</div></div>
  <div class="cell"><div class="shift s-grey">10:00 - 19:00</div></div>
  <div class="cell"><div class="shift s-grey">10:00 - 19:00</div></div>

  <div class="person"><div class="badge" style="background:var(--amber)"><svg width="16" height="16" viewBox="0 0 16 16"><circle cx="8" cy="5" r="3.2"/><path d="M2 15c0-3.5 2.7-5.5 6-5.5s6 2 6 5.5z"/></svg></div><div><b>01 Employee</b><span>Branch B | Department 6</span></div></div>
  <div class="hrs">30</div>
  <div class="cell"><div class="shift s-sky">10:00 - 19:00</div></div>
  <div class="cell"><div class="shift s-peach">10:00 - 19:00</div></div>
  <div class="cell"><div class="shift s-purple">10:00 - 19:00</div></div>
  <div class="cell"><div class="shift s-teal">10:00 - 19:00</div></div>
  <div class="cell"><div class="shift s-sky">10:00 - 19:00</div></div>
  <div class="cell"><div class="shift s-grey">10:00 - 19:00</div></div>
  <div class="cell"><div class="shift s-grey">10:00 - 19:00</div></div>

  <div class="person"><div class="badge" style="background:var(--navy)"><svg width="16" height="16" viewBox="0 0 16 16"><circle cx="8" cy="5" r="3.2"/><path d="M2 15c0-3.5 2.7-5.5 6-5.5s6 2 6 5.5z"/></svg></div><div><b>01 Employee</b><span>Branch B | Department 6</span></div></div>
  <div class="hrs">0</div>
  <div class="cell"></div><div class="cell"></div><div class="cell"></div><div class="cell"></div><div class="cell"></div><div class="cell"></div><div class="cell"></div>

  <div class="person"><div class="badge" style="background:var(--orange)"><svg width="16" height="16" viewBox="0 0 16 16"><circle cx="8" cy="5" r="3.2"/><path d="M2 15c0-3.5 2.7-5.5 6-5.5s6 2 6 5.5z"/></svg></div><div><b>01 Employee</b><span>Branch B | Department 6</span></div></div>
  <div class="hrs">0</div>
  <div class="cell"></div><div class="cell"></div><div class="cell"></div><div class="cell"></div><div class="cell"></div><div class="cell"></div><div class="cell"></div>

  <div class="person"><div class="badge" style="background:#4a7ef0"><svg width="16" height="16" viewBox="0 0 16 16"><circle cx="8" cy="5" r="3.2"/><path d="M2 15c0-3.5 2.7-5.5 6-5.5s6 2 6 5.5z"/></svg></div><div><b>01 Employee</b><span>Branch B | Department 6</span></div></div>
  <div class="hrs">0</div>
  <div class="cell"></div><div class="cell"></div><div class="cell"></div><div class="cell"></div><div class="cell"></div><div class="cell"></div><div class="cell"></div>

  <div class="person"><div class="badge" style="background:#b057e8"><svg width="16" height="16" viewBox="0 0 16 16"><circle cx="8" cy="5" r="3.2"/><path d="M2 15c0-3.5 2.7-5.5 6-5.5s6 2 6 5.5z"/></svg></div><div><b>01 Employee</b><span>Branch B | Department 6</span></div></div>
  <div class="hrs">0</div>
  <div class="cell"></div><div class="cell"></div><div class="cell"></div><div class="cell"></div><div class="cell"></div><div class="cell"></div><div class="cell"></div>

  <div class="person"><div class="badge" style="background:var(--amber)"><svg width="16" height="16" viewBox="0 0 16 16"><circle cx="8" cy="5" r="3.2"/><path d="M2 15c0-3.5 2.7-5.5 6-5.5s6 2 6 5.5z"/></svg></div><div><b>01 Employee</b><span>Branch B | Department 6</span></div></div>
  <div class="hrs">0</div>
  <div class="cell"></div><div class="cell"></div><div class="cell"></div><div class="cell"></div><div class="cell"></div><div class="cell"></div><div class="cell"></div>

  <div class="person"><div class="badge" style="background:var(--navy)"><svg width="16" height="16" viewBox="0 0 16 16"><circle cx="8" cy="5" r="3.2"/><path d="M2 15c0-3.5 2.7-5.5 6-5.5s6 2 6 5.5z"/></svg></div><div><b>01 Employee</b><span>Branch B | Department 6</span></div></div>
  <div class="hrs">0</div>
  <div class="cell"></div><div class="cell"></div><div class="cell"></div><div class="cell"></div><div class="cell"></div><div class="cell"></div><div class="cell"></div>

  <div class="person"><div class="badge" style="background:var(--orange)"><svg width="16" height="16" viewBox="0 0 16 16"><circle cx="8" cy="5" r="3.2"/><path d="M2 15c0-3.5 2.7-5.5 6-5.5s6 2 6 5.5z"/></svg></div><div><b>01 Employee</b><span>Branch B | Department 6</span></div></div>
  <div class="hrs">0</div>
  <div class="cell"></div><div class="cell"></div><div class="cell"></div><div class="cell"></div><div class="cell"></div><div class="cell"></div><div class="cell"></div>

  <div class="person"><div class="badge" style="background:#4a7ef0"><svg width="16" height="16" viewBox="0 0 16 16"><circle cx="8" cy="5" r="3.2"/><path d="M2 15c0-3.5 2.7-5.5 6-5.5s6 2 6 5.5z"/></svg></div><div><b>01 Employee</b><span>Branch B | Department 6</span></div></div>
  <div class="hrs">0</div>
  <div class="cell"></div><div class="cell"></div><div class="cell"></div><div class="cell"></div><div class="cell"></div><div class="cell"></div><div class="cell"></div>
</div>
</body>
</html>
```